Medical Device Company needs website

We are a start-up medical device company looking to sell boot (foot) and brace (ankle) products on Shopify. We are still working on the name but you can use Kaltir as a placeholder- no logo yet)

Website information:
- Look: modern/tech with clean lines and symmetry.
- Colors: teal, white, black, and greys.
- Headers: home, shop, about us, help, blog
- Icons (upper right): search, my account and shopping cart
-place to sign up for newsletter

```html
<!DOCTYPE html>
<html lang="en">
<head>
<meta charset="utf-8">
<title>Kaltir – Healthy Feet</title>
<link href="https://fonts.googleapis.com/css2?family=Montserrat:wght@400;500;600&display=swap" rel="stylesheet">
<style>
:root{
  --teal:#1fc7cf;
  --ink:#1c1c1c;
  --text:#3a3a3a;
  --muted:#8a8a8a;
  --line:#e6e6e6;
  --white:#ffffff;
  --red:#d5262a;
  --green:#3d9a3a;
  --star:#f5b301;
}
*{box-sizing:border-box;margin:0;padding:0}
html,body{width:1200px;height:3575px;overflow:hidden}
body{position:relative;background:var(--white);font-family:"Montserrat",sans-serif;color:var(--text)}
.abs{position:absolute}
.site-header{left:0;top:0;width:1200px;height:66px;background:linear-gradient(90deg,#eef8f8,#e5f6f7 60%,#eaf6f8)}
.logo{left:170px;top:21px;display:flex;align-items:center;gap:6px;font-weight:600;font-size:15px;color:var(--ink)}
.logo-dot{width:14px;height:14px;border-radius:50%;background:var(--teal)}
.nav{left:271px;top:25px;display:flex;gap:22px;font-size:11.5px;color:#555;white-space:nowrap}
.nav .active{color:var(--ink);text-decoration:underline;text-underline-offset:3px}
.header-icons{left:934px;top:22px;display:flex;gap:15px}
.hero{left:0;top:84px;width:1200px;height:703px;background:linear-gradient(180deg,#f2eff0 0%,#ede9ea 70%,#c9bdb6 86%,#b7a99f 100%)}
.hero-photo{right:0;top:0;width:760px;height:703px;background:linear-gradient(120deg,rgba(0,0,0,0) 20%,#8c8f93 50%,#3a3c40 75%,#5d6066 100%);opacity:.85}
.hero-title{left:131px;top:314px;font-size:55px;font-weight:500;color:var(--ink);letter-spacing:-.5px;white-space:nowrap}
.hero-sub{left:131px;top:389px;font-size:31px;font-weight:400;color:var(--ink);white-space:nowrap}
.hero-desc{left:131px;top:466px;font-size:13px;color:#555;white-space:nowrap}
.btn{background:var(--ink);color:var(--white);font-size:11px;font-weight:600;display:flex;align-items:center;justify-content:center;border-radius:3px;letter-spacing:.3px}
.hero-btn{left:131px;top:523px;width:117px;height:39px}
.cat-photo{background:linear-gradient(160deg,#f6ece6,#d9c6b9 50%,#3e3f44)}
.cat-label{font-size:19px;font-weight:500;color:var(--ink)}
.section-title{left:0;width:1200px;text-align:center;font-size:31px;font-weight:500;color:var(--ink)}
.product-img{border-radius:2px}
.product-name{font-size:13px;color:var(--ink);text-align:center;width:222px;white-space:nowrap}
.product-price{font-size:11.5px;color:#666;text-align:center;width:222px;white-space:nowrap}
.product-price s{margin-left:6px}
.divider{height:1px;background:var(--line)}
.feature{width:320px;text-align:center}
.feature h3{font-size:16px;font-weight:500;color:var(--ink);margin:14px 0 12px}
.feature p{font-size:12.5px;color:var(--muted);line-height:18px;padding:0 45px}
.buy-card{left:600px;top:1881px;width:468px;height:597px;border:1px solid var(--line);border-radius:12px}
.stars{color:var(--star);letter-spacing:2px}
.thumb{width:101px;height:101px;border-radius:4px;background:linear-gradient(180deg,#f4f4f6,#d9dbe0)}
.pay{width:38px;height:24px;border-radius:3px;border:1px solid var(--line)}
.perk{font-size:13px;color:var(--text);display:flex;align-items:center;gap:8px;white-space:nowrap}
.price-row{left:637px;top:2036px;display:flex;align-items:center;gap:8px;white-space:nowrap}
.price-now{font-size:20px;font-weight:500;color:var(--ink)}
.badge{background:var(--red);color:#fff;font-size:10px;font-weight:600;padding:5px 12px;border-radius:12px}
.review{width:297px;height:368px;border:1px solid #f0f0f0;border-radius:4px;padding:38px 36px 0}
.review h4{font-size:12.5px;font-weight:600;color:var(--ink);margin:18px 0 16px;white-space:nowrap}
.review p{font-size:11px;line-height:17.5px;color:#444}
.review .who{font-size:11.5px;font-weight:600;color:var(--ink);margin-top:22px}
.review .from{font-size:11px;color:var(--muted);margin-top:14px}
.review .mini{border-top:1px solid var(--line);margin-top:24px;padding-top:22px;display:flex;align-items:center;gap:14px;font-size:10.5px}
.mini-img{width:44px;height:44px;background:linear-gradient(180deg,#eef0f3,#cfd3d8);border-radius:3px}
.newsletter{left:0;top:3090px;width:1200px;height:485px;background:#b9bac0}
.news-photo{left:412px;top:0;width:190px;height:485px;background:linear-gradient(90deg,#d8d3c8,#f3efe6 40%,#c9a27f 100%);opacity:.9}
.news-title{left:131px;top:3220px;font-size:44px;font-weight:600;color:var(--ink);white-space:nowrap}
.news-sub{left:131px;top:3282px;font-size:24px;color:var(--ink);white-space:nowrap}
.news-desc{left:131px;top:3330px;font-size:12.5px;color:#666;white-space:nowrap}
.news-input{left:131px;top:3383px;width:235px;height:31px;background:var(--white);border:1px solid #ddd;border-radius:3px;font-size:11px;color:#888;padding:9px 12px}
.news-btn{left:373px;top:3383px;width:118px;height:31px}
</style>
</head>
<body>

<header class="abs site-header">
  <div class="abs logo"><span class="logo-dot"></span>Kaltir</div>
  <nav class="abs nav"><span class="active">Home</span><span>Shop</span><span>About Us</span><span>Help</span><span>Blog</span></nav>
  <div class="abs header-icons">
    <svg width="20" height="20" viewBox="0 0 20 20" fill="none" stroke="#333" stroke-width="1.4"><circle cx="8.5" cy="8.5" r="5.5"/><path d="M13 13l4 4"/></svg>
    <svg width="20" height="20" viewBox="0 0 20 20" fill="none" stroke="#333" stroke-width="1.4"><circle cx="10" cy="7" r="3.5"/><path d="M3.5 17c1-3.5 3.5-5 6.5-5s5.5 1.5 6.5 5z"/></svg>
    <svg width="20" height="20" viewBox="0 0 20 20" fill="none" stroke="#333" stroke-width="1.4"><path d="M4 6h12l-1 11H5z"/><path d="M7.5 8V5a2.5 2.5 0 015 0v3"/></svg>
  </div>
</header>

<section class="abs hero">
  <div class="abs hero-photo" role="img" aria-label="Athlete in grey sportswear stretching in a lunge, running shoe in the foreground"></div>
</section>
<h1 class="abs hero-title">Healthy Feet</h1>
<p class="abs hero-sub">Confident Steps</p>
<p class="abs hero-desc">Discover the Precision, Comfort, and Style of Our Premium Feet Medical Solutions</p>
<div class="abs btn hero-btn">SHOP NOW</div>

<div class="abs cat-photo" style="left:208px;top:812px;width:150px;height:172px" role="img" aria-label="Legs wearing a sneaker and a black walking boot"></div>
<span class="abs cat-label" style="left:156px;top:958px">Boot</span>
<svg class="abs" style="left:382px;top:964px" width="14" height="14" viewBox="0 0 14 14" fill="none" stroke="#222" stroke-width="1.4"><path d="M2 7h10M8 3l4 4-4 4"/></svg>
<div class="abs cat-photo" style="left:845px;top:812px;width:223px;height:188px;background:linear-gradient(150deg,#fff,#f4e6dc 50%,#c9a28a)" role="img" aria-label="Foot with an elastic bandage wrapped around the ankle"></div>
<span class="abs cat-label" style="left:798px;top:958px">Brace</span>
<svg class="abs" style="left:1024px;top:964px" width="14" height="14" viewBox="0 0 14 14" fill="none" stroke="#222" stroke-width="1.4"><path d="M2 7h10M8 3l4 4-4 4"/></svg>

<h2 class="abs section-title" style="top:1103px">Explore Our Products</h2>

<div class="abs product-img" style="left:131px;top:1183px;width:222px;height:240px;background:linear-gradient(180deg,#fff,#e9ebee 55%,#c9f1f3)" role="img" aria-label="White medical walking boot with teal sole"></div>
<p class="abs product-name" style="left:131px;top:1440px">Smart Medical Boot</p>
<p class="abs product-price" style="left:131px;top:1466px">$350.00 USD<s>$500.00 USD</s></p>

<div class="abs product-img" style="left:369px;top:1183px;width:222px;height:236px;background:linear-gradient(180deg,#efeff1,#cfd1d6)" role="img" aria-label="Grey and black medical walking boot"></div>
<p class="abs product-name" style="left:369px;top:1432px">Smart Medical Boot 2</p>
<p class="abs product-price" style="left:369px;top:1457px">$350.00 USD<s>$500.00 USD</s></p>

<div class="abs product-img" style="left:607px;top:1183px;width:222px;height:240px;background:linear-gradient(180deg,#fff,#e9ebee 60%,#c9f1f3)" role="img" aria-label="Tall white medical walking boot with teal sole"></div>
<p class="abs product-name" style="left:607px;top:1444px">Smart Medical Boot 3</p>
<p class="abs product-price" style="left:607px;top:1469px">$350.00 USD<s>$500.00 USD</s></p>

<div class="abs product-img" style="left:846px;top:1183px;width:222px;height:248px;background:linear-gradient(180deg,#fff,#e3e3e5 30%,#3a3b3f 70%,#f4f4f4)" role="img" aria-label="Tall black medical walking boot"></div>
<p class="abs product-name" style="left:846px;top:1450px">Smart Medical Boot 4</p>
<p class="abs product-price" style="left:846px;top:1475px">$350.00 USD<s>$500.00 USD</s></p>

<div class="abs divider" style="left:131px;top:1559px;width:937px"></div>

<div class="abs feature" style="left:119px;top:1626px">
  <svg width="40" height="40" viewBox="0 0 40 40" fill="none" stroke="var(--teal)" stroke-width="1.4"><path d="M8 34C14 22 22 12 34 6c-2 12-10 22-22 24M14 26l8-8M18 29l6-6"/></svg>
  <h3>Lightweight Design</h3>
  <p>Made from durable materials that won't weigh you down.</p>
</div>
<div class="abs feature" style="left:440px;top:1626px">
  <svg width="40" height="40" viewBox="0 0 40 40" fill="none" stroke="var(--teal)" stroke-width="1.4"><rect x="6" y="5" width="16" height="30" rx="2"/><rect x="26" y="10" width="6" height="20" rx="3"/><path d="M29 5v5M29 30v5M11 28h6"/></svg>
  <h3>Adjustable Straps</h3>
  <p>Get the perfect fit every time, no matter your size.</p>
</div>
<div class="abs feature" style="left:760px;top:1626px">
  <svg width="40" height="40" viewBox="0 0 40 40" fill="none" stroke="var(--teal)" stroke-width="1.4"><circle cx="21" cy="7" r="3"/><path d="M20 12l-4 10 6 4-2 10M18 16l-6 4M21 14l5 6 5-1M16 22l-4 13"/></svg>
  <h3>Shock Absorption</h3>
  <p>Cushioned sole absorbs impact so you can move without worry.</p>
</div>

<div class="abs" style="left:195px;top:1885px;width:350px;height:460px;background:linear-gradient(180deg,#fff,#eceef1 45%,#d5d8dd 80%,#bff0f2)" role="img" aria-label="White medical walking boot with teal sole and air pump"></div>
<svg class="abs" style="left:147px;top:2127px" width="10" height="14" viewBox="0 0 10 14" fill="none" stroke="#bbb" stroke-width="1.3"><path d="M7 2L2 7l5 5"/></svg>
<svg class="abs" style="left:549px;top:2127px" width="10" height="14" viewBox="0 0 10 14" fill="none" stroke="#333" stroke-width="1.3"><path d="M3 2l5 5-5 5"/></svg>
<div class="abs thumb" style="left:131px;top:2378px;border:1px solid #999" role="img" aria-label="White boot thumbnail"></div>
<div class="abs thumb" style="left:245px;top:2378px;background:linear-gradient(180deg,#fff,#3c3d41 60%,#fff)" role="img" aria-label="Black boot thumbnail"></div>
<div class="abs thumb" style="left:360px;top:2378px;background:linear-gradient(180deg,#eeeff1,#c7cad0)" role="img" aria-label="Grey boot thumbnail"></div>
<div class="abs thumb" style="left:474px;top:2378px" role="img" aria-label="Tall white boot thumbnail"></div>

<div class="abs buy-card"></div>
<div class="abs" style="left:637px;top:1919px;font-size:12px;display:flex;gap:6px;align-items:center;white-space:nowrap"><span class="stars">★★★★★</span><span>5.0 (975 reviews)</span></div>
<p class="abs" style="left:637px;top:1956px;font-size:19px;font-weight:600;color:var(--ink);white-space:nowrap">Smart Medical Boot</p>
<div class="abs divider" style="left:637px;top:1998px;width:394px"></div>
<p class="abs" style="left:637px;top:2018px;font-size:12px;color:#aaa"><s>$500.00 USD</s></p>
<div class="abs price-row"><span class="price-now">$350.00 USD</span><span class="badge">Save 30%</span></div>
<div class="abs" style="left:637px;top:2078px;width:95px;height:38px;border:1px solid #ddd;display:flex;justify-content:space-around;align-items:center;font-size:12px;color:var(--ink)"><span>−</span><span>1</span><span>+</span></div>
<div class="abs btn" style="left:746px;top:2078px;width:285px;height:38px">ADD TO CART</div>
<div class="abs" style="left:637px;top:2135px;display:flex;gap:9px">
  <span class="pay" style="background:#eef0f7"></span><span class="pay" style="background:#e8f0fa"></span><span class="pay" style="background:#fbeee7"></span><span class="pay" style="background:#e1ecf8"></span><span class="pay" style="background:#eef3fa"></span>
</div>
<div class="abs divider" style="left:637px;top:2176px;width:394px"></div>
<div class="abs perk" style="left:637px;top:2195px"><svg width="18" height="14" viewBox="0 0 18 14" fill="#222"><rect x="0" y="2" width="11" height="8"/><path d="M11 5h4l3 3v2h-7z"/><circle cx="4" cy="11.5" r="2"/><circle cx="14" cy="11.5" r="2"/></svg><span>You have qualified for <span style="color:var(--green)">FREE SHIPPING</span></span></div>
<div class="abs perk" style="left:637px;top:2233px"><svg width="18" height="16" viewBox="0 0 18 16" fill="#222"><path d="M1 6l8-5 8 5v9H1z"/><rect x="5" y="8" width="8" height="7" fill="#fff"/></svg><span>Leaves warehouse in <span style="color:var(--green)">1-2 business days</span></span></div>
<div class="abs perk" style="left:637px;top:2271px"><svg width="18" height="16" viewBox="0 0 18 16" fill="#222"><path d="M9 1l7 4v6l-7 4-7-4V5z"/></svg><span>Comes with a 12 Month Warranty <span style="text-decoration:underline">Learn more.</span></span></div>

<h2 class="abs section-title" style="top:2555px">Hear from Our Happy Customers</h2>

<article class="abs review" style="left:131px;top:2640px">
  <div class="stars" style="font-size:13px">★★★★★</div>
  <h4>Highly Recommend!</h4>
  <p>"The ergonomic design has made a huge difference in my daily comfort. I can type for hours without any discomfort."</p>
  <p class="who">Marco Lindell</p>
  <p class="from">Customer from Singapore</p>
  <div class="mini"><span class="mini-img" role="img" aria-label="Boot thumbnail"></span><div><div style="color:var(--ink)">Smart Medical Boot</div><div style="color:var(--red);margin-top:5px">$350.00 USD</div><div style="color:#bbb"><s>$500.00 USD</s></div></div></div>
</article>
<article class="abs review" style="left:452px;top:2640px">
  <div class="stars" style="font-size:13px">★★★★★</div>
  <h4>Fantastic Selection and Service</h4>
  <p>"This keyboard has completely transformed my typing experience. The build quality is superb and the tactile feedback is perfect!"</p>
  <p class="who">Hana R</p>
  <p class="from">Customer from USA</p>
  <div class="mini"><span class="mini-img" role="img" aria-label="Boot thumbnail"></span><div><div style="color:var(--ink)">Smart Medical Boot</div><div style="color:var(--red);margin-top:5px">$350.00 USD</div><div style="color:#bbb"><s>$500.00 USD</s></div></div></div>
</article>
<article class="abs review" style="left:772px;top:2640px">
  <div class="stars" style="font-size:13px">★★★★★</div>
  <h4>Great Quality and Fast Shipping</h4>
  <p>"As a gamer, I appreciate the fast response times and customizable lighting. It's a game-changer for my setup."</p>
  <p class="who">Priya T.</p>
  <p class="from">Customer from China</p>
  <div class="mini"><span class="mini-img" role="img" aria-label="Boot thumbnail"></span><div><div style="color:var(--ink)">Smart Medical Boot</div><div style="color:var(--red);margin-top:5px">$350.00 USD</div><div style="color:#bbb"><s>$500.00 USD</s></div></div></div>
</article>

<section class="abs newsletter">
  <div class="abs news-photo" role="img" aria-label="Close-up of a white ankle brace strap"></div>
</section>
<h2 class="abs news-title">Stay Updated</h2>
<p class="abs news-sub">with Our Newsletter</p>
<p class="abs news-desc">Get the Latest News, Deals, and Tips Straight to Your Inbox</p>
<div class="abs news-input">Your email</div>
<div class="abs btn news-btn">SUBSCRIBE</div>

</body>
</html>
```